Create a business promotion flyer to leave in customer mailboxes. We are a bulk petroleum supplier, servicing any industry that requires diesel. Base in griffith NSW, servicing griffith area and surrounds.

Business Name - Terra Diesel
Fuel@terradiesel-example.com.au
Marco - 0412 309 768 mpellucci@terradiesel-example.com.au
Liam - 0431 672 095 lhartwell@terradiesel-example.com.au
Simon - 0465 218 347 sbrack@terradiesel-example.com.au
Office 02 6931 7852

Bulk Fuel deliveries.
Oils & lubricants
Local Family owned business

```html
<!DOCTYPE html>
<html lang="en">
<head>
<meta charset="utf-8">
<title>Terra Diesel – Bulk Fuel Flyer</title>
<link href="https://fonts.googleapis.com/css2?family=Montserrat:wght@500;600;700&family=Roboto+Condensed:wght@500;700&display=swap" rel="stylesheet">
<style>
  :root{
    --black:#070707;
    --red:#c8161a;
    --red-dark:#a50f12;
    --white:#ffffff;
    --ink:#141414;
    --paper:#f7f7f7;
    --earth:#2b241d;
  }
  *{margin:0;padding:0;box-sizing:border-box}
  html,body{width:933px;height:1200px;overflow:hidden;background:var(--paper)}
  .flyer{width:933px;height:1200px;display:flex;flex-direction:column;font-family:"Montserrat",sans-serif;color:var(--ink)}

  .masthead{height:309px;background:var(--black);display:flex;align-items:center;justify-content:center;gap:22px}
  .brand-mark{width:34px;height:34px;background:var(--red);border-radius:50%}
  .brand-name{font-family:"Montserrat",sans-serif;font-weight:600;font-size:92px;color:var(--white);letter-spacing:-1px}

  .values-band{height:60px;background:linear-gradient(90deg,var(--red-dark),var(--red) 50%,var(--red-dark));display:flex;align-items:center;justify-content:center;gap:26px;color:var(--white);font-family:"Roboto Condensed",sans-serif;font-weight:700;font-size:20px;letter-spacing:.3px}
  .value{display:flex;align-items:center;gap:12px}
  .value svg{width:30px;height:30px}
  .band-divider{width:1px;height:30px;background:rgba(255,255,255,.45);transform:skewX(-20deg)}

  .truck-photo{height:225px;background:linear-gradient(180deg,#8fb2d6 0%,#c7cfd6 38%,#e9ebec 62%,#b9b7b2 100%)}

  .intro{height:92px;display:flex;flex-direction:column;align-items:center;justify-content:center;font-size:17.5px;font-weight:500;line-height:1.6;text-align:center;background:var(--white)}
  .intro strong{color:var(--red);font-weight:700}

  .service-area{height:342px;display:flex;background:var(--white)}
  .region-panel{width:407px;background:radial-gradient(circle at 60% 30%,#3a3027,var(--earth) 55%,#141210);display:flex;flex-direction:column}
  .region-map{flex:1}
  .region-text{padding:0 20px 20px;text-align:center;color:var(--white)}
  .region-title{font-family:"Roboto Condensed",sans-serif;font-weight:700;font-size:26px;line-height:1.13;text-transform:uppercase}
  .region-sub{font-size:13px;line-height:1.3;margin-top:10px}

  .contacts{flex:1;padding:22px 0 0 52px;display:flex;flex-direction:column;gap:14px}
  .contact{display:flex;align-items:center;gap:28px}
  .contact-icon{width:58px;height:58px;flex:none;border-radius:50%;background:var(--red);display:flex;align-items:center;justify-content:center}
  .contact-icon svg{width:32px;height:24px}
  .contact-line{font-size:25px;font-weight:600;color:var(--red);line-height:1.2}
  .contact-email{font-size:16.5px;font-weight:500;color:var(--ink);margin-top:3px}

  .spacer{height:26px;background:var(--white)}

  .services{height:147px;background:var(--black);display:flex;align-items:center;justify-content:center;gap:26px;color:var(--white);font-family:"Roboto Condensed",sans-serif;font-weight:700;font-size:22px;line-height:1.3;text-transform:uppercase}
  .service{display:flex;align-items:center;gap:24px}
  .service svg{height:58px}
  .service-divider{width:2px;height:92px;background:var(--white);transform:skewX(-20deg)}
</style>
</head>
<body>
<main class="flyer">
  <header class="masthead">
    <span class="brand-mark"></span>
    <h1 class="brand-name">Terra Diesel</h1>
  </header>

  <section class="values-band">
    <div class="value">
      <svg viewBox="0 0 24 24" fill="none" stroke="#fff" stroke-width="1.8" stroke-linejoin="round"><path d="M12 2l8 3v6c0 5-3.5 9-8 11-4.5-2-8-6-8-11V5z"/><path d="M8 12l3 3 5-6" stroke-linecap="round"/></svg>
      <span>RELIABLE SUPPLY</span>
    </div>
    <span class="band-divider"></span>
    <div class="value">
      <svg viewBox="0 0 24 24" fill="none" stroke="#fff" stroke-width="1.8"><circle cx="12" cy="7" r="4.5"/><path d="M3 23v-3a6 6 0 0 1 6-6h6a6 6 0 0 1 6 6v3z"/></svg>
      <span>LOCAL EXPERTISE</span>
    </div>
    <span class="band-divider"></span>
    <div class="value">
      <svg viewBox="0 0 32 24" fill="#fff"><circle cx="16" cy="6" r="4"/><circle cx="6" cy="8" r="3.2"/><circle cx="26" cy="8" r="3.2"/><path d="M9 22v-4a5 5 0 0 1 5-5h4a5 5 0 0 1 5 5v4z"/><path d="M0 21v-3a4 4 0 0 1 4-4h5a7 7 0 0 0-2 4v3z"/><path d="M32 21v-3a4 4 0 0 0-4-4h-5a7 7 0 0 1 2 4v3z"/></svg>
      <span>FAMILY OWNED</span>
    </div>
  </section>

  <div class="truck-photo" role="img" aria-label="Photo of a white B-double fuel tanker truck parked in front of a depot shed under a blue sky"></div>

  <section class="intro">
    <p><strong>Terra Diesel</strong> We are a bulk petroleum supplier, servicing any industry that requires diesel.</p>
    <p>Based in <strong>Griffith</strong> NSW, servicing Griffith area and surrounds.</p>
  </section>

  <section class="service-area">
    <div class="region-panel">
      <div class="region-map" role="img" aria-label="Map of New South Wales marking Griffith and nearby service towns"></div>
      <div class="region-text">
        <h2 class="region-title">Available across<br>Griffith and<br>surrounding areas</h2>
        <p class="region-sub">Local expertise and resources<br>ready for projects<br>across the region.</p>
      </div>
    </div>

    <div class="contacts">
      <div class="contact">
        <span class="contact-icon"><svg viewBox="0 0 32 24" fill="none" stroke="#fff" stroke-width="2"><rect x="1" y="1" width="30" height="22"/><path d="M1 1l15 12 15-12M1 23l11-10M31 23L20 13"/></svg></span>
        <div><p class="contact-line">Office 02 6931 7852</p><p class="contact-email">Fuel@terradiesel-example.com.au</p></div>
      </div>
      <div class="contact">
        <span class="contact-icon"><svg viewBox="0 0 32 24" fill="none" stroke="#fff" stroke-width="2"><rect x="1" y="1" width="30" height="22"/><path d="M1 1l15 12 15-12M1 23l11-10M31 23L20 13"/></svg></span>
        <div><p class="contact-line">Marco - 0412 309 768</p><p class="contact-email">mpellucci@terradiesel-example.com.au</p></div>
      </div>
      <div class="contact">
        <span class="contact-icon"><svg viewBox="0 0 32 24" fill="none" stroke="#fff" stroke-width="2"><rect x="1" y="1" width="30" height="22"/><path d="M1 1l15 12 15-12M1 23l11-10M31 23L20 13"/></svg></span>
        <div><p class="contact-line">Liam - 0431 672 095</p><p class="contact-email">lhartwell@terradiesel-example.com.au</p></div>
      </div>
      <div class="contact">
        <span class="contact-icon"><svg viewBox="0 0 32 24" fill="none" stroke="#fff" stroke-width="2"><rect x="1" y="1" width="30" height="22"/><path d="M1 1l15 12 15-12M1 23l11-10M31 23L20 13"/></svg></span>
        <div><p class="contact-line">Simon - 0465 218 347</p><p class="contact-email">sbrack@terradiesel-example.com.au</p></div>
      </div>
    </div>
  </section>

  <div class="spacer"></div>

  <footer class="services">
    <div class="service">
      <svg viewBox="0 0 40 42" fill="#fff"><path d="M3 4a3 3 0 0 1 3-3h14a3 3 0 0 1 3 3v34h2v3H1v-3h2z"/><rect x="7" y="5" width="12" height="9" fill="#070707"/><path d="M23 10l6 5v16a2 2 0 0 0 4 0V14l-4-5" fill="none" stroke="#fff" stroke-width="2.5" stroke-linejoin="round"/></svg>
      <span>Bulk fuel<br>deliveries</span>
    </div>
    <span class="service-divider"></span>
    <div class="service">
      <svg viewBox="0 0 30 42" fill="#fff"><path d="M15 0C11 10 2 19 2 28a13 13 0 0 0 26 0C28 19 19 10 15 0z"/><path d="M9 27a7 7 0 0 0 7 9" fill="none" stroke="#070707" stroke-width="2.5" stroke-linecap="round"/></svg>
      <span>Oils &amp;<br>lubricants</span>
    </div>
    <span class="service-divider"></span>
    <div class="service">
      <svg viewBox="0 0 56 40" fill="#fff"><circle cx="17" cy="9" r="8"/><circle cx="40" cy="9" r="8"/><path d="M0 40v-7a13 13 0 0 1 13-13h8a13 13 0 0 1 13 13v7z"/><path d="M24 40v-7a13 13 0 0 1 13-13h6a13 13 0 0 1 13 13v7z"/></svg>
      <span>Local family<br>owned business</span>
    </div>
  </footer>
</main>
</body>
</html>
```